Book Cover Design

Design with title UNWAVERING
Subtitle: Ways to Kindle the Spark of Resolve
Author Name: Carla Jean Morrow
Put DAILY MERIDIAN BESTSELLER at top
Shimmer design, see inspirational images attached

```html
<!DOCTYPE html>
<html lang="en">
<head>
<meta charset="utf-8">
<title>Unwavering — Book Cover</title>
<link rel="stylesheet" href="https://fonts.googleapis.com/css2?family=Oswald:wght@600&family=Open+Sans:wght@400;700&display=swap">
<style>
  :root {
    --page-bg: #ffffff;
    --ink: #0d0d0d;
    --holo-cyan: #9fefff;
    --holo-sky: #8fd3ff;
    --holo-magenta: #f56ff0;
    --holo-violet: #b06cf4;
    --holo-pink: #f7a2e2;
    --holo-cream: #f8e6bb;
    --holo-rose: #f087d4;
    --holo-lilac: #c79cf0;
    --holo-mint: #d9f1c8;
  }
  html, body {
    margin: 0;
    padding: 0;
    width: 1200px;
    height: 1200px;
    overflow: hidden;
    background: var(--page-bg);
  }
  .canvas {
    position: relative;
    width: 1200px;
    height: 1200px;
    display: flex;
    align-items: center;
    justify-content: center;
  }
  .book-cover {
    position: relative;
    width: 740px;
    height: 1080px;
    box-sizing: border-box;
    color: var(--ink);
    text-align: center;
    background:
      linear-gradient(180deg, rgba(255,255,255,0.35) 0%, rgba(255,255,255,0) 30%, rgba(255,255,255,0) 75%, rgba(255,255,255,0.2) 100%),
      linear-gradient(90deg,
        var(--holo-cyan) 0%,
        var(--holo-sky) 6%,
        var(--holo-magenta) 14%,
        var(--holo-violet) 22%,
        var(--holo-sky) 30%,
        var(--holo-pink) 38%,
        var(--holo-magenta) 44%,
        var(--holo-cream) 52%,
        var(--holo-mint) 58%,
        var(--holo-pink) 66%,
        var(--holo-cream) 72%,
        var(--holo-rose) 80%,
        var(--holo-lilac) 88%,
        var(--holo-rose) 94%,
        var(--holo-violet) 100%);
  }
  .bestseller-line {
    position: absolute;
    top: 60px;
    left: 0;
    right: 0;
    margin: 0;
    font-family: "Open Sans", sans-serif;
    font-weight: 400;
    font-size: 34px;
    letter-spacing: 0.5px;
  }
  .title {
    position: absolute;
    top: 430px;
    left: 0;
    right: 0;
    margin: 0;
    font-family: "Oswald", sans-serif;
    font-weight: 600;
    font-size: 112px;
    line-height: 1;
    letter-spacing: 2px;
  }
  .subtitle {
    position: absolute;
    top: 570px;
    left: 60px;
    right: 60px;
    margin: 0;
    font-family: "Open Sans", sans-serif;
    font-weight: 400;
    font-size: 36px;
    line-height: 1.2;
  }
  .author {
    position: absolute;
    bottom: 110px;
    left: 0;
    right: 0;
    margin: 0;
    font-family: "Open Sans", sans-serif;
    font-weight: 700;
    font-size: 40px;
  }
</style>
</head>
<body>
  <main class="canvas">
    <section class="book-cover" role="img" aria-label="Book cover with iridescent holographic shimmer background">
      <p class="bestseller-line">DAILY MERIDIAN BESTSELLER</p>
      <h1 class="title">UNWAVERING</h1>
      <p class="subtitle">Ways to Kindle<br>the Spark of Resolve</p>
      <p class="author">Carla Jean Morrow</p>
    </section>
  </main>
</body>
</html>
```